Brindell Excavation and Landscaping

I need a double sided card thick with rounded edges. I want an identical card of one of your designs but with my name on it on one side. Othe side I want my name,number under owner operator and a list of what I do. , drainage,grading,trenching stump removal , postholes. Landscaping lawn renovations, and reconfigurations, small to large rip outs and installs,sod work and burms and swails for water run off and plantings the two pictures of cards is what I like

Reason: First time doing this not sure if two days was enough, no one was taking on project so trying to figure out why I posted a picture of what I want so should be relatively easy

Industry/Entity Type

Landscaping

Contact Information for Business Card

Name Ted Brindell
Harbor Point County Phone 860-555-0143

Font styles to use
Other font styles liked:
• It's on card I sent second one

Requirements
Must have
• Same colors and look of card at bottom
Nice to have
• All aspects of excavation and landscaping on back of card
• Will add web address at end

```html
<!DOCTYPE html>
<html lang="en">
<head>
<meta charset="utf-8">
<title>Brindell Excavation and Landscaping – Business Card</title>
<link rel="stylesheet" href="https://fonts.googleapis.com/css2?family=Krona+One&family=Exo+2:ital,wght@1,400;1,500&family=Montserrat:wght@700;800&display=swap">
<style>
  :root {
    --backdrop: #4d4d4d;
    --card-white: #ffffff;
    --card-dark: #262626;
    --accent-orange: #f26b30;
    --accent-green: #8dc63f;
    --ink: #262626;
    --logo-grey: #7d7d7d;
    --tagline-grey: #d4d4d4;
  }
  * { margin: 0; padding: 0; box-sizing: border-box; }
  html, body { width: 1200px; height: 1000px; overflow: hidden; background: var(--backdrop); }
  .canvas { position: relative; width: 1200px; height: 1000px; }
  .card-shape { position: absolute; left: 0; top: 0; }

  .holder-name {
    position: absolute; right: 730px; top: 410px;
    font-family: "Krona One", sans-serif; font-size: 31px; color: var(--ink);
    letter-spacing: 1.5px; white-space: nowrap; font-weight: 400;
  }
  .holder-role {
    position: absolute; right: 732px; top: 447px;
    font-family: "Montserrat", sans-serif; font-weight: 800; font-size: 22px;
    color: var(--accent-orange); letter-spacing: 0.5px;
  }
  .contact-list { position: absolute; right: 732px; top: 560px; list-style: none; }
  .contact-item {
    display: flex; align-items: center; justify-content: flex-end; gap: 8px;
    font-family: "Montserrat", sans-serif; font-weight: 800; color: var(--ink);
    white-space: nowrap;
  }
  .contact-item svg { fill: var(--accent-orange); flex: none; }
  .contact-phone { font-size: 31px; height: 36px; letter-spacing: 0.5px; }
  .contact-area { font-size: 21px; height: 32px; }
  .contact-email { font-size: 22px; height: 34px; font-weight: 700; }

  .brand { position: absolute; left: 610px; width: 410px; top: 336px; text-align: center; }
  .brand-name {
    font-family: "Krona One", sans-serif; font-size: 52px; color: var(--logo-grey);
    letter-spacing: 2px; line-height: 1;
  }
  .brand-sub {
    margin-top: 10px; font-family: "Montserrat", sans-serif; font-weight: 700;
    font-size: 12px; letter-spacing: 5.6px; color: var(--logo-grey); white-space: nowrap;
  }
  .tagline {
    position: absolute; left: 520px; width: 590px; top: 505px; text-align: center;
    font-family: "Exo 2", sans-serif; font-style: italic; font-weight: 500;
    font-variant: small-caps; font-size: 30px; line-height: 31px; color: var(--tagline-grey);
  }
  .tagline-highlight { display: block; color: var(--accent-green); }
  .credentials {
    position: absolute; left: 520px; width: 590px; top: 731px; text-align: center;
    font-family: "Exo 2", sans-serif; font-style: italic; font-weight: 400;
    font-size: 21px; letter-spacing: 8px; color: var(--accent-orange);
  }
</style>
</head>
<body>
<main class="canvas">
  <svg class="card-shape" width="1200" height="1000" viewBox="0 0 1200 1000" aria-hidden="true">
    <defs>
      <clipPath id="card-clip">
        <rect x="78" y="220" width="1050" height="600" rx="70" ry="70"/>
      </clipPath>
    </defs>
    <g clip-path="url(#card-clip)">
      <rect class="card-front" x="78" y="220" width="1050" height="600" fill="var(--card-white)"/>
      <path class="card-band" d="M450,220 C505,380 522,560 486,820 L1128,820 L1128,220 Z" fill="var(--accent-green)"/>
      <path class="card-panel" d="M488,220 C522,380 528,560 488,820 L1128,820 L1128,220 Z" fill="var(--card-dark)"/>
      <rect class="name-tab" x="78" y="406" width="43" height="69" fill="var(--card-dark)"/>
    </g>
  </svg>

  <h1 class="holder-name">TED BRINDELL</h1>
  <p class="holder-role">owner</p>

  <ul class="contact-list">
    <li class="contact-item contact-phone">
      <svg width="24" height="28" viewBox="0 0 24 24"><path d="M6.6 10.8a15 15 0 0 0 6.6 6.6l2.2-2.2c.3-.3.7-.4 1-.2 1.1.4 2.3.6 3.6.6.6 0 1 .4 1 1V20c0 .6-.4 1-1 1A17 17 0 0 1 3 4c0-.6.4-1 1-1h3.5c.6 0 1 .4 1 1 0 1.3.2 2.5.6 3.6.1.3 0 .7-.2 1z"/></svg>
      860-555-0143
    </li>
    <li class="contact-item contact-area">
      <svg width="18" height="28" viewBox="0 0 18 28"><path d="M9 0a9 9 0 0 0-9 9c0 7 9 19 9 19s9-12 9-19a9 9 0 0 0-9-9zm0 12.5A3.5 3.5 0 1 1 9 5.5a3.5 3.5 0 0 1 0 7z"/></svg>
      HARBOR POINT COUNTY
    </li>
    <li class="contact-item contact-email">
      <svg width="26" height="18" viewBox="0 0 26 18"><path d="M0 0h26v18H0zM2 2.5v13h22v-13L13 10z" fill-rule="evenodd"/><path d="M2 2h22L13 9.5z"/></svg>
      ted.brindell@example.com
    </li>
  </ul>

  <div class="brand">
    <p class="brand-name">BRINDELL</p>
    <p class="brand-sub">EXCAVATION AND LANDSCAPING</p>
  </div>

  <p class="tagline">Specializing in all aspects of residential
    <span class="tagline-highlight">Excavation and Landscaping</span></p>

  <p class="credentials">LICENSED AND INSURED</p>
</main>
</body>
</html>
```